E-Sport banner for team [logo already created]

Hey,

Need a 2400 x 600 banner for our esport team we are creating.
The logo is already created, what we need is to make a banner out of it.

So, the logo shouldn't stay exactly the same, you should be creative and do something special with it.

Banner should be:
Clean
Modern
Have kinda the same theme as the logo provided
Be creative

Example of banners (not the same size):
https://i.plomvid.com/vi/Kq7RtbWmLo2/maxresdefault.jpg
https://i.plomvid.com/vi/Hn3_vaPeQz5/maxresdefault.jpg
https://i.plomvid.com/vi/ruwYkTdoBcN/maxresdefault.jpg
https://i.plomvid.com/vi/pLo8gWxjRtA/maxresdefault.jpg

Check here for even more inspiration:
https://sketchvane.com/tags/esports_banner

```html
<!DOCTYPE html>
<html lang="en">
<head>
<meta charset="utf-8">
<title>Kestran Gaming – E-Sportcenter Banner</title>
<link href="https://fonts.googleapis.com/css2?family=Rajdhani:wght@300;500&display=swap" rel="stylesheet">
<style>
  :root {
    --navy-deep: #060f22;
    --navy: #0d1f3d;
    --navy-glow: #1b3a66;
    --flare: #5fa8ff;
    --silver: #c9cacf;
    --emblem: #2a3344;
    --accent: #fbf93a;
    --ink: #111111;
  }
  * { margin: 0; padding: 0; box-sizing: border-box; }
  html, body { width: 1200px; height: 300px; overflow: hidden; background: var(--navy-deep); }
  .banner {
    position: relative;
    width: 1200px;
    height: 300px;
    overflow: hidden;
    background:
      radial-gradient(ellipse 420px 260px at 640px 170px, rgba(27,58,102,0.55), transparent 70%),
      radial-gradient(ellipse 500px 300px at 180px 140px, rgba(27,58,102,0.6), transparent 70%),
      linear-gradient(180deg, var(--navy-deep) 0%, var(--navy) 100%);
    font-family: "Rajdhani", sans-serif;
  }
  .flare {
    position: absolute;
    left: 0; top: 127px;
    width: 700px; height: 3px;
    background: linear-gradient(90deg, transparent 0%, rgba(95,168,255,0.5) 25%, rgba(180,215,255,0.9) 46%, rgba(95,168,255,0.5) 62%, transparent 100%);
    filter: blur(1px);
  }
  .flare-core {
    position: absolute;
    left: 260px; top: 98px;
    width: 120px; height: 60px;
    background: radial-gradient(ellipse at center, rgba(120,180,255,0.45), transparent 70%);
  }
  .emblem {
    position: absolute;
    left: 155px; top: 55px;
    width: 170px; height: 170px;
    border-radius: 50%;
    background: var(--emblem);
  }
  .team-name {
    position: absolute;
    left: 414px; top: 72px;
    font-weight: 300;
    font-size: 88px;
    line-height: 1;
    letter-spacing: 3px;
    color: var(--silver);
    white-space: nowrap;
  }
  .tag {
    position: absolute;
    left: 523px; top: 188px;
    width: 357px; height: 45px;
    background: var(--accent);
    transform: skewX(-5deg);
    display: flex;
    align-items: center;
    justify-content: center;
  }
  .tag-text {
    font-weight: 500;
    font-size: 27px;
    letter-spacing: 11px;
    color: var(--ink);
    text-transform: uppercase;
    padding-left: 11px;
  }
</style>
</head>
<body>
  <div class="banner">
    <div class="flare"></div>
    <div class="flare-core"></div>
    <div class="emblem" aria-hidden="true"></div>
    <h1 class="team-name">KESTRAN GAMING</h1>
    <div class="tag"><span class="tag-text">E-Sportcenter</span></div>
  </div>
</body>
</html>
```